Business Card desgin, company called Stand Fast.

I am looking for the logo colors (3) to be used on the card in whatever design you think might work. the certifications are on the back (4) on the front will be my name, Dana Whitlock, owner/instructor, phone 208.555.0193, website www.sfx-drills.example, email dw@sfx-drills.example. im flexible on fonts.

Target Market(s)

firearms owners

Industry/Entity Type

firearms training

Contact Information for Business Card

certification icons on back

```html
<!DOCTYPE html>
<html lang="en">
<head>
<meta charset="utf-8">
<title>Stand Fast — Business Card</title>
<link rel="stylesheet" href="https://fonts.googleapis.com/css2?family=Chakra+Petch:wght@400;700&family=Montserrat:wght@800&display=swap">
<style>
  :root {
    --navy: #0b2942;
    --red: #c0272d;
    --white: #ffffff;
    --stage: #9a9a9a;
    --grey-text: #8c8c8c;
    --rule: #9d9d9d;
    --star: #f2a51c;
    --badge-front: #e9edf2;
    --badge-back: #2a2a2a;
    --faint: #ecd9d2;
  }
  * { margin: 0; padding: 0; box-sizing: border-box; }
  html, body { width: 1200px; height: 1000px; overflow: hidden; }
  body { background: var(--stage); position: relative; font-family: "Chakra Petch", sans-serif; }

  .card { position: absolute; width: 732px; height: 422px; border-radius: 24px; overflow: hidden; }
  .card--front { left: 233px; top: 46px; background: var(--navy); }
  .card--back { left: 232px; top: 519px; background: var(--white); }

  /* front */
  .front-mark { position: absolute; left: 307px; top: 66px; }
  .front-name {
    position: absolute; left: 0; right: 0; top: 180px; text-align: center;
    font-family: "Montserrat", sans-serif; font-weight: 800; font-size: 58px;
    color: var(--white); letter-spacing: 1px; line-height: 1;
  }
  .web-band {
    position: absolute; left: 142px; top: 251px; width: 446px; height: 36px;
    background: linear-gradient(90deg, rgba(192,39,45,0) 0%, var(--red) 8%, var(--red) 92%, rgba(192,39,45,0) 100%);
    display: flex; align-items: center; justify-content: center;
    font-weight: 700; font-size: 21px; letter-spacing: 2.5px; color: var(--navy);
  }
  .cert-row {
    position: absolute; left: 160px; top: 318px; width: 420px; height: 66px;
    display: flex; align-items: center; justify-content: space-between;
  }
  .cert-badge { width: 64px; height: 62px; }
  .cert-badge--shield { border-radius: 10px 10px 32px 32px; width: 56px; }
  .cert-badge--wing { border-radius: 14px 14px 28px 28px; }
  .cert-badge--round { border-radius: 50%; width: 58px; height: 58px; }
  .card--front .cert-badge { background: var(--badge-front); }
  .star { width: 14px; height: 14px; }

  /* back */
  .back-watermark { position: absolute; left: 290px; top: 40px; }
  .back-brand { position: absolute; left: 32px; top: 50px; display: flex; align-items: center; gap: 12px; }
  .back-brand__name { font-family: "Montserrat", sans-serif; font-weight: 800; font-size: 25px; color: var(--navy); }
  .person { position: absolute; left: 32px; top: 228px; }
  .person__name { font-weight: 700; font-size: 33px; color: var(--navy); line-height: 1.05; }
  .person__role { font-size: 22px; color: var(--red); letter-spacing: 0.5px; line-height: 1.1; }
  .divider { position: absolute; left: 32px; top: 304px; width: 665px; height: 1px; background: var(--rule); }
  .contact { position: absolute; left: 32px; top: 330px; font-size: 22px; line-height: 31px; color: var(--grey-text); }
  .contact__key { color: var(--red); font-weight: 700; }
  .cert-row--back { left: 358px; top: 330px; width: 340px; height: 62px; }
  .card--back .cert-badge { background: var(--badge-back); width: 52px; height: 56px; }
  .card--back .cert-badge--round { background: var(--navy); width: 52px; height: 52px; }
  .card--back .cert-badge--shield { background: #e9792a; width: 50px; }
</style>
</head>
<body>

<section class="card card--front" aria-label="Card front">
  <svg class="front-mark" width="118" height="118" viewBox="0 0 118 118" aria-hidden="true">
    <circle cx="59" cy="59" r="48" fill="none" stroke="var(--white)" stroke-width="8"/>
  </svg>
  <div class="front-name">STAND FAST</div>
  <div class="web-band">WWW.SFX-DRILLS.EXAMPLE</div>
  <div class="cert-row" aria-label="Certifications">
    <div class="cert-badge cert-badge--shield"></div>
    <svg class="star" viewBox="0 0 24 24" aria-hidden="true"><path fill="var(--white)" d="M12 2l3 7h7l-5.6 4.3 2 7.2L12 16.3 5.6 20.5l2-7.2L2 9h7z"/></svg>
    <div class="cert-badge cert-badge--wing"></div>
    <svg class="star" viewBox="0 0 24 24" aria-hidden="true"><path fill="var(--white)" d="M12 2l3 7h7l-5.6 4.3 2 7.2L12 16.3 5.6 20.5l2-7.2L2 9h7z"/></svg>
    <div class="cert-badge cert-badge--wing"></div>
    <svg class="star" viewBox="0 0 24 24" aria-hidden="true"><path fill="var(--white)" d="M12 2l3 7h7l-5.6 4.3 2 7.2L12 16.3 5.6 20.5l2-7.2L2 9h7z"/></svg>
    <div class="cert-badge cert-badge--round"></div>
  </div>
</section>

<section class="card card--back" aria-label="Card back">
  <svg class="back-watermark" width="520" height="520" viewBox="0 0 520 520" aria-hidden="true">
    <circle cx="260" cy="260" r="250" fill="none" stroke="var(--faint)" stroke-width="2"/>
  </svg>
  <div class="back-brand">
    <svg width="46" height="46" viewBox="0 0 46 46" aria-hidden="true">
      <circle cx="23" cy="23" r="19" fill="none" stroke="var(--navy)" stroke-width="5"/>
    </svg>
    <span class="back-brand__name">STAND FAST</span>
  </div>
  <div class="person">
    <div class="person__name">Dana Whitlock</div>
    <div class="person__role">owner/instructor</div>
  </div>
  <div class="divider"></div>
  <div class="contact">
    <div><span class="contact__key">p:</span> 208.555.0193</div>
    <div><span class="contact__key">e:</span> dw@sfx-drills.example</div>
  </div>
  <div class="cert-row cert-row--back" aria-label="Certifications">
    <div class="cert-badge cert-badge--shield"></div>
    <svg class="star" viewBox="0 0 24 24" aria-hidden="true"><path fill="var(--star)" d="M12 2l3 7h7l-5.6 4.3 2 7.2L12 16.3 5.6 20.5l2-7.2L2 9h7z"/></svg>
    <div class="cert-badge cert-badge--wing"></div>
    <svg class="star" viewBox="0 0 24 24" aria-hidden="true"><path fill="var(--star)" d="M12 2l3 7h7l-5.6 4.3 2 7.2L12 16.3 5.6 20.5l2-7.2L2 9h7z"/></svg>
    <div class="cert-badge cert-badge--wing"></div>
    <svg class="star" viewBox="0 0 24 24" aria-hidden="true"><path fill="var(--star)" d="M12 2l3 7h7l-5.6 4.3 2 7.2L12 16.3 5.6 20.5l2-7.2L2 9h7z"/></svg>
    <div class="cert-badge cert-badge--round"></div>
  </div>
</section>

</body>
</html>
```